you will use Ai to Copy the website Quellabyx.com to come up with the basic frame work and it will give you the understanding of how I would like Zandoprik.com to be like. Zandoprik.com is a peer to peer rv rental site very similar to both of the other rv rental sites the difference is that are commission based 20% and above per rental and we will be one flat monthly rate and they keep all the earnings. Below is photo that will help you with the color scheme and the look and feel of the design

```html
<!DOCTYPE html>
<html lang="en">
<head>
<meta charset="utf-8">
<title>Zandoprik.com — Rent An RV. Keep Every Dollar You Earn.</title>
<link href="https://fonts.googleapis.com/css2?family=Libre+Caslon+Text:wght@400;700&family=Montserrat:wght@400;500;600;700&display=swap" rel="stylesheet">
<style>
:root{
  --navy:#15214a;
  --navy-deep:#0f1a3c;
  --green:#4b9a40;
  --green-btn:#3f9446;
  --cream:#f2f0e9;
  --sage:#e4ecdc;
  --ink:#1d2433;
  --muted:#6b7280;
  --star:#e7a019;
  --line:#dcdcd4;
  --white:#ffffff;
}
*{box-sizing:border-box;margin:0;padding:0}
html,body{width:1200px;height:4110px;overflow:hidden}
body{font-family:"Montserrat",sans-serif;color:var(--ink);
  background:linear-gradient(180deg,var(--cream) 0,var(--cream) 900px,var(--sage) 1700px,#eef3ea 2250px,#fbfcfa 2500px,#ffffff 3372px)}
.page{position:relative;width:1200px;height:4110px}
.abs{position:absolute}

/* header */
.brand{left:115px;top:24px;font-weight:700;font-size:24px;color:var(--navy);display:flex;align-items:center;gap:8px}
.brand .dot{width:12px;height:12px;border-radius:50%;background:var(--green)}
.nav{top:38px;left:500px;display:flex;gap:24px;font-size:10px;font-weight:600;letter-spacing:.3px}
.nav a{color:var(--navy);text-decoration:none}
.nav a.active{border-bottom:2px solid var(--green);padding-bottom:5px}
.nav a.dim{color:#566;font-weight:500}
.btn-list{left:894px;top:29px;width:115px;height:32px;border-radius:16px;background:var(--green-btn);color:#fff;font-size:10px;font-weight:700;display:flex;align-items:center;justify-content:center;letter-spacing:.3px}
.menu-icon{left:1027px;top:36px}
.user-icon{left:1055px;top:31px;width:28px;height:28px;border-radius:50%;background:#fff;border:1px solid var(--line);display:flex;align-items:center;justify-content:center}

.hero-title{left:115px;top:124px;font-family:"Libre Caslon Text",serif;font-size:54px;line-height:63px;font-weight:700;color:var(--navy);letter-spacing:-1.5px}

/* search */
.search{left:115px;top:287px;width:970px;height:90px;border-radius:45px;background:#fff;box-shadow:0 6px 20px rgba(20,30,60,.07)}
.field{position:absolute;top:18px}
.field .lbl{font-size:8px;letter-spacing:1.2px;color:#8a8f99;font-weight:600}
.field .val{font-size:11px;color:var(--ink);margin-top:16px;font-weight:500}
.divider{position:absolute;top:0;width:1px;height:90px;background:#eee}
.search-go{position:absolute;right:12px;top:11px;width:68px;height:68px;border-radius:50%;background:var(--navy);display:flex;align-items:center;justify-content:center}

/* hero cards */
.promo{top:425px;width:480px;height:322px;border-radius:10px;overflow:hidden}
.promo .photo{position:absolute;inset:0}
.promo .shade{position:absolute;inset:0;background:linear-gradient(180deg,rgba(0,0,0,0) 35%,rgba(0,0,0,.55) 100%)}
.promo h3{position:absolute;left:27px;top:162px;font-family:"Libre Caslon Text",serif;font-weight:700;color:#fff;font-size:28px;line-height:32px;letter-spacing:-.5px}
.promo p{position:absolute;left:27px;top:233px;color:#f2f2f2;font-size:10.5px}
.promo .pill{position:absolute;left:27px;top:265px;height:30px;padding:0 22px;border-radius:15px;background:#fff;color:var(--navy);font-size:9.5px;font-weight:700;display:flex;align-items:center;letter-spacing:.3px}

/* section heads */
.h2{font-family:"Libre Caslon Text",serif;color:var(--navy);font-size:42px;line-height:47px;letter-spacing:-1px;font-weight:400}
.sub{font-size:11.5px;color:var(--ink)}

.filters{top:890px;left:790px;display:flex;gap:12px}
.chip{height:37px;border-radius:19px;background:#fff;border:1px solid #e6e6e0;display:flex;align-items:center;gap:6px;padding:0 20px;font-size:10px;font-weight:600;color:var(--navy)}
.chip.on{background:var(--navy);color:#fff;border-color:var(--navy)}

/* rv cards */
.grid{left:113px;width:974px;display:grid;grid-template-columns:repeat(4,232px);column-gap:15px}
.rv .img{position:relative;height:166px;border-radius:9px;overflow:hidden}
.rv .badge{position:absolute;left:10px;top:10px;background:var(--green);color:#fff;font-size:7.5px;font-weight:700;padding:5px 9px;border-radius:10px;letter-spacing:.3px}
.rv .fav{position:absolute;right:10px;top:8px;width:22px;height:22px;border-radius:50%;background:var(--green);display:flex;align-items:center;justify-content:center}
.rv .dots{position:absolute;left:0;right:0;bottom:10px;display:flex;justify-content:center;gap:4px}
.rv .dots i{width:4px;height:4px;border-radius:50%;background:rgba(255,255,255,.75)}
.rv .dots i:first-child{background:#fff}
.rv .body{padding:18px 14px 0 15px}
.rv .title{font-size:12px;font-weight:600;color:var(--ink);white-space:nowrap}
.rv .meta{display:flex;justify-content:space-between;margin-top:12px;font-size:9.5px;color:#444}
.rv .meta span{display:flex;align-items:center;gap:5px}
.rv .meta b{font-weight:600;color:var(--ink)}
.rv .specs{display:flex;gap:14px;margin-top:16px;font-size:9.5px;color:#444}
.rv .specs span{display:flex;align-items:center;gap:5px}
.rv .price{margin-top:16px;font-size:18px;font-weight:700;color:var(--ink)}
.rv .price small{font-size:9.5px;font-weight:500;color:#444;margin-left:5px}

.btn-navy{height:35px;border-radius:18px;background:var(--navy);color:#fff;font-size:9.5px;font-weight:700;letter-spacing:.4px;display:flex;align-items:center;justify-content:center}

/* parks */
.parks{top:1938px;left:113px;display:flex;gap:7px}
.park{position:relative;width:238px;height:330px;border-radius:6px;overflow:hidden}
.park .photo{position:absolute;inset:0}
.park .shade{position:absolute;inset:0;background:linear-gradient(180deg,rgba(0,0,0,0) 45%,rgba(0,0,0,.55) 100%)}
.park .info{position:absolute;left:0;right:0;top:205px;text-align:center;color:#fff}
.park h4{font-family:"Libre Caslon Text",serif;font-weight:700;font-size:22px;letter-spacing:-.5px}
.park p{font-size:11.5px;margin-top:10px}
.park p b{font-weight:700}
.park .pill{display:inline-flex;margin-top:12px;height:32px;padding:0 28px;border-radius:16px;background:#fff;color:var(--navy);font-size:9px;font-weight:700;align-items:center}

/* destination lists */
.dest{left:112px;width:1000px;display:grid;grid-template-columns:repeat(7,146px);row-gap:24px}
.dest div{font-size:10px;color:var(--navy);font-weight:500;line-height:14px}
.dest div span{display:block;color:#8a8f99;font-weight:400;font-size:9.5px}

/* owners band */
.band{left:0;top:3372px;width:1200px;height:331px;background:var(--green);overflow:hidden}
.band h2{position:absolute;left:113px;top:80px;font-family:"Libre Caslon Text",serif;font-size:42px;line-height:47px;color:#fff;font-weight:400;letter-spacing:-1px}
.band p{position:absolute;left:113px;top:182px;width:460px;color:#fff;font-size:11.5px;line-height:18px}
.band .pill{position:absolute;left:113px;top:238px;width:136px;height:34px;border-radius:17px;background:#fff;color:var(--navy);font-size:9.5px;font-weight:700;display:flex;align-items:center;justify-content:center}
.ring{position:absolute;border-radius:50%;border:1px solid rgba(255,255,255,.18)}
.stat{position:absolute;left:793px;top:80px;width:166px;height:166px;border-radius:50%;background:#fff;text-align:center;padding-top:46px}
.stat strong{display:block;font-size:38px;font-weight:700;color:var(--green);letter-spacing:-1px;line-height:40px}
.stat span{display:block;font-size:10px;font-weight:700;color:var(--navy);letter-spacing:1px;line-height:13px;margin-top:4px}

/* footer */
.footer{left:0;top:3703px;width:1200px;height:407px;background:var(--navy-deep);color:#fff}
.footer .fbrand{position:absolute;left:113px;top:84px;font-size:24px;font-weight:700;display:flex;align-items:center;gap:8px}
.footer .fbrand .dot{width:12px;height:12px;border-radius:50%;background:var(--green)}
.footer .tag{position:absolute;left:113px;top:140px;font-family:"Libre Caslon Text",serif;font-size:18px;line-height:27px;color:#e8ebf3}
.footer .rule{position:absolute;left:113px;top:207px;width:225px;height:1px;background:rgba(255,255,255,.18)}
.footer .dl{position:absolute;left:116px;top:225px;font-size:9px;letter-spacing:1.3px;font-weight:600;color:#d4d8e4}
.store{position:absolute;top:253px;height:24px;border-radius:5px;background:#000;border:1px solid #555}
.col{position:absolute;top:86px}
.col h5{font-family:"Libre Caslon Text",serif;font-size:17px;font-weight:400;color:#fff}
.col ul{list-style:none;margin-top:26px}
.col li{font-size:11px;color:#c9cedb;line-height:24px}
.footer .bottom{position:absolute;left:113px;top:343px;width:974px;height:1px;background:rgba(255,255,255,.14)}
.footer .copy{position:absolute;left:113px;top:369px;font-size:10.5px;color:#c9cedb}
.social{position:absolute;top:364px;left:966px;display:flex;gap:14px}
.social i{display:block;width:19px;height:19px;border-radius:4px;background:#fff}
.social i.round{border-radius:50%}
</style>
</head>
<body>
<div class="page">

<header>
  <div class="abs brand"><span class="dot"></span>Zandoprik.com</div>
  <nav class="abs nav">
    <a class="active" href="#">RV RENTALS</a>
    <a class="dim" href="#">FIND A CAMPGROUND</a>
  </nav>
  <div class="abs btn-list">LIST YOUR RV</div>
  <svg class="abs menu-icon" width="18" height="16" viewBox="0 0 18 16"><rect y="1" width="18" height="2" rx="1" fill="#15214a"/><rect y="7" width="18" height="2" rx="1" fill="#15214a"/><rect y="13" width="18" height="2" rx="1" fill="#15214a"/></svg>
  <div class="abs user-icon"><svg width="16" height="16" viewBox="0 0 16 16" fill="none" stroke="#15214a" stroke-width="1.5"><circle cx="8" cy="8" r="7"/><circle cx="8" cy="6.5" r="2.3"/><path d="M3.5 13c1.2-2 2.7-2.8 4.5-2.8s3.3.8 4.5 2.8"/></svg></div>
</header>

<h1 class="abs hero-title">Rent An RV. Keep<br>Every Dollar You Earn.</h1>

<form class="abs search">
  <div class="field" style="left:53px"><div class="lbl">LOCATION</div><div class="val">Joshua Tree,USA</div></div>
  <div class="divider" style="left:319px"></div>
  <div class="field" style="left:338px"><div class="lbl">DATES</div><div class="val">Any Dates</div></div>
  <div class="divider" style="left:460px"></div>
  <div class="field" style="left:479px"><div class="lbl">GUEST</div><div class="val">2 Guests</div></div>
  <div class="divider" style="left:598px"></div>
  <div class="field" style="left:618px;width:230px"><div class="lbl">RV TYPE</div><div class="val" style="display:flex;justify-content:space-between">All Types <svg width="9" height="6" viewBox="0 0 9 6"><path d="M1 1l3.5 3.5L8 1" stroke="#555" fill="none" stroke-width="1.2"/></svg></div></div>
  <div class="search-go"><svg width="26" height="26" viewBox="0 0 26 26" fill="none" stroke="#fff" stroke-width="2.2"><circle cx="12" cy="12" r="8"/><path d="M18 18l5 5"/></svg></div>
</form>

<section>
  <div class="abs promo" style="left:113px">
    <div class="photo" role="img" aria-label="Motorhome parked in a pine forest campsite at golden hour" style="background:linear-gradient(160deg,#c9b58a 0%,#7e6b47 30%,#3f4a2c 60%,#26301e 100%)"></div>
    <div class="shade"></div>
    <h3>Drive or Tow<br>Your Adventure</h3>
    <p>Choose from drivable RVs and towable trailers across the country.</p>
    <div class="pill">EXPLORE RVS</div>
  </div>
  <div class="abs promo" style="left:607px">
    <div class="photo" role="img" aria-label="SUV towing a travel trailer beside a mountain lake" style="background:linear-gradient(175deg,#b9c6c3 0%,#6f8a7a 25%,#3e6a66 45%,#4f6b3b 70%,#34452a 100%)"></div>
    <div class="shade"></div>
    <h3>RV Delivery<br>Made Easy</h3>
    <p>Get your RV delivered and set up at your campsite or event.</p>
    <div class="pill">EXPLORE DELIVERY</div>
  </div>
</section>

<section>
  <h2 class="abs h2" style="left:115px;top:842px">Find the Perfect<br>RV for yourAdventure</h2>
  <p class="abs sub" style="left:115px;top:950px">Explore the open road in the perfect RV rental. Or, get one delivered And set up for you.</p>
  <div class="abs filters">
    <div class="chip on"><svg width="11" height="10" viewBox="0 0 12 11"><path d="M6 10S1 7 1 3.6A2.6 2.6 0 0 1 6 2.4a2.6 2.6 0 0 1 5 1.2C11 7 6 10 6 10z" fill="none" stroke="#fff" stroke-width="1.2"/></svg>Popular</div>
    <div class="chip"><svg width="11" height="11" viewBox="0 0 12 12"><path d="M6 1l1.3 3.7L11 6 7.3 7.3 6 11 4.7 7.3 1 6l3.7-1.3z" fill="none" stroke="#15214a" stroke-width="1.1"/></svg>New</div>
    <div class="chip"><svg width="13" height="10" viewBox="0 0 14 10"><rect x="1" y="1" width="12" height="6" rx="1" fill="none" stroke="#15214a" stroke-width="1.1"/><circle cx="4" cy="8.5" r="1.2" fill="#15214a"/><circle cx="10" cy="8.5" r="1.2" fill="#15214a"/></svg>Vintage</div>
  </div>

  <div class="abs grid" style="top:1017px">
    <article class="rv">
      <div class="img" role="img" aria-label="Class A motorhome on a forest road" style="background:linear-gradient(170deg,#9fb3a6,#5c5443 55%,#3a3428)"><span class="badge">TOP RATED</span><span class="fav"><svg width="10" height="9" viewBox="0 0 12 11"><path d="M6 10S1 7 1 3.6A2.6 2.6 0 0 1 6 2.4a2.6 2.6 0 0 1 5 1.2C11 7 6 10 6 10z" fill="#fff"/></svg></span><div class="dots"><i></i><i></i><i></i><i></i><i></i><i></i></div></div>
      <div class="body"><div class="title">2022 Halvorne Ridgeway 30KT</div>
      <div class="meta"><span><svg width="9" height="11" viewBox="0 0 10 12"><path d="M5 11S1 6.6 1 4.3a4 4 0 0 1 8 0C9 6.6 5 11 5 11z" fill="none" stroke="#555"/><circle cx="5" cy="4.3" r="1.3" fill="#555"/></svg>Denver, CO</span><span><svg width="10" height="10" viewBox="0 0 10 10"><path d="M5 .5l1.4 2.9 3.1.4-2.3 2.2.6 3.1L5 7.6 2.2 9.1l.6-3.1L.5 3.8l3.1-.4z" fill="#e7a019"/></svg><b>5.0</b> (24)</span></div>
      <div class="specs"><span><svg width="11" height="9" viewBox="0 0 12 10"><path d="M1 9V1M1 6h10v3M3 6V4h4v2" fill="none" stroke="#555"/></svg>Sleeps 6</span><span><svg width="11" height="9" viewBox="0 0 12 10"><rect x=".5" y="1.5" width="11" height="7" fill="none" stroke="#555"/><path d="M3 1.5v3M6 1.5v3M9 1.5v3" stroke="#555"/></svg>29 ft</span><span><svg width="12" height="9" viewBox="0 0 13 10"><rect x=".5" y=".5" width="9" height="6.5" fill="none" stroke="#555"/><path d="M9.5 3H12v4H9.5" fill="none" stroke="#555"/><circle cx="3" cy="8.5" r="1" fill="#555"/><circle cx="10" cy="8.5" r="1" fill="#555"/></svg>Class A</span></div>
      <div class="price">$189<small>/ night</small></div></div>
    </article>
    <article class="rv">
      <div class="img" role="img" aria-label="Travel trailer parked among tall pines" style="background:linear-gradient(170deg,#c9d2c6,#6f7f5a 50%,#3d4a2f)"><div class="dots"><i></i><i></i><i></i><i></i><i></i><i></i></div></div>
      <div class="body"><div class="title">2021 Brisco Pinecrest 26QB</div>
      <div class="meta"><span><svg width="9" height="11" viewBox="0 0 10 12"><path d="M5 11S1 6.6 1 4.3a4 4 0 0 1 8 0C9 6.6 5 11 5 11z" fill="none" stroke="#555"/><circle cx="5" cy="4.3" r="1.3" fill="#555"/></svg>Austin, TX</span><span><svg width="10" height="10" viewBox="0 0 10 10"><path d="M5 .5l1.4 2.9 3.1.4-2.3 2.2.6 3.1L5 7.6 2.2 9.1l.6-3.1L.5 3.8l3.1-.4z" fill="#e7a019"/></svg><b>4.9</b> (18)</span></div>
      <div class="specs"><span><svg width="11" height="9" viewBox="0 0 12 10"><path d="M1 9V1M1 6h10v3M3 6V4h4v2" fill="none" stroke="#555"/></svg>Sleeps 8</span><span><svg width="11" height="9" viewBox="0 0 12 10"><rect x=".5" y="1.5" width="11" height="7" fill="none" stroke="#555"/><path d="M3 1.5v3M6 1.5v3M9 1.5v3" stroke="#555"/></svg>28 ft</span><span><svg width="12" height="9" viewBox="0 0 13 10"><rect x=".5" y=".5" width="9" height="6.5" fill="none" stroke="#555"/><path d="M9.5 3H12v4H9.5" fill="none" stroke="#555"/><circle cx="3" cy="8.5" r="1" fill="#555"/><circle cx="10" cy="8.5" r="1" fill="#555"/></svg>Travel Trailer</span></div>
      <div class="price">$129<small>/ night</small></div></div>
    </article>
    <article class="rv">
      <div class="img" role="img" aria-label="Camper van beside a mountain lake" style="background:linear-gradient(170deg,#8fb3cf,#6d8b7c 50%,#4c5e3a)"><span class="badge">TOP RATED</span><span class="fav"><svg width="10" height="9" viewBox="0 0 12 11"><path d="M6 10S1 7 1 3.6A2.6 2.6 0 0 1 6 2.4a2.6 2.6 0 0 1 5 1.2C11 7 6 10 6 10z" fill="#fff"/></svg></span><div class="dots"><i></i><i></i><i></i><i></i><i></i><i></i></div></div>
      <div class="body"><div class="title">2020 Korvel Nomad 170</div>
      <div class="meta"><span><svg width="9" height="11" viewBox="0 0 10 12"><path d="M5 11S1 6.6 1 4.3a4 4 0 0 1 8 0C9 6.6 5 11 5 11z" fill="none" stroke="#555"/><circle cx="5" cy="4.3" r="1.3" fill="#555"/></svg>Portland, OR</span><span><svg width="10" height="10" viewBox="0 0 10 10"><path d="M5 .5l1.4 2.9 3.1.4-2.3 2.2.6 3.1L5 7.6 2.2 9.1l.6-3.1L.5 3.8l3.1-.4z" fill="#e7a019"/></svg><b>5.0</b> (22)</span></div>
      <div class="specs"><span><svg width="11" height="9" viewBox="0 0 12 10"><path d="M1 9V1M1 6h10v3M3 6V4h4v2" fill="none" stroke="#555"/></svg>Sleeps 4</span><span><svg width="11" height="9" viewBox="0 0 12 10"><rect x=".5" y="1.5" width="11" height="7" fill="none" stroke="#555"/><path d="M3 1.5v3M6 1.5v3M9 1.5v3" stroke="#555"/></svg>21 ft</span><span><svg width="12" height="9" viewBox="0 0 13 10"><rect x=".5" y=".5" width="9" height="6.5" fill="none" stroke="#555"/><path d="M9.5 3H12v4H9.5" fill="none" stroke="#555"/><circle cx="3" cy="8.5" r="1" fill="#555"/><circle cx="10" cy="8.5" r="1" fill="#555"/></svg>Van</span></div>
      <div class="price">$159<small>/ night</small></div></div>
    </article>
    <article class="rv">
      <div class="img" role="img" aria-label="Class C motorhome among autumn trees and mountains" style="background:linear-gradient(170deg,#a9bcc8,#c48a3b 45%,#5f5a3a)"><div class="dots"><i></i><i></i><i></i><i></i><i></i><i></i></div></div>
      <div class="body"><div class="title">2023 Tarven Summit 29RX</div>
      <div class="meta"><span><svg width="9" height="11" viewBox="0 0 10 12"><path d="M5 11S1 6.6 1 4.3a4 4 0 0 1 8 0C9 6.6 5 11 5 11z" fill="none" stroke="#555"/><circle cx="5" cy="4.3" r="1.3" fill="#555"/></svg>Nashville, TN</span><span><svg width="10" height="10" viewBox="0 0 10 10"><path d="M5 .5l1.4 2.9 3.1.4-2.3 2.2.6 3.1L5 7.6 2.2 9.1l.6-3.1L.5 3.8l3.1-.4z" fill="#e7a019"/></svg><b>4.8</b> (21)</span></div>
      <div class="specs"><span><svg width="11" height="9" viewBox="0 0 12 10"><path d="M1 9V1M1 6h10v3M3 6V4h4v2" fill="none" stroke="#555"/></svg>Sleeps 7</span><span><svg width="11" height="9" viewBox="0 0 12 10"><rect x=".5" y="1.5" width="11" height="7" fill="none" stroke="#555"/><path d="M3 1.5v3M6 1.5v3M9 1.5v3" stroke="#555"/></svg>31 ft</span><span><svg width="12" height="9" viewBox="0 0 13 10"><rect x=".5" y=".5" width="9" height="6.5" fill="none" stroke="#555"/><path d="M9.5 3H12v4H9.5" fill="none" stroke="#555"/><circle cx="3" cy="8.5" r="1" fill="#555"/><circle cx="10" cy="8.5" r="1" fill="#555"/></svg>Class C</span></div>
      <div class="price">$175<small>/ night</small></div></div>
    </article>
  </div>

  <div class="abs grid" style="top:1390px">
    <article class="rv">
      <div class="img" role="img" aria-label="Class A motorhome on a forest road" style="background:linear-gradient(170deg,#9fb3a6,#5c5443 55%,#3a3428)"><div class="dots"><i></i><i></i><i></i><i></i><i></i><i></i></div></div>
      <div class="body"><div class="title">2022 Halvorne Ridgeway 30KT</div>
      <div class="meta"><span><svg width="9" height="11" viewBox="0 0 10 12"><path d="M5 11S1 6.6 1 4.3a4 4 0 0 1 8 0C9 6.6 5 11 5 11z" fill="none" stroke="#555"/><circle cx="5" cy="4.3" r="1.3" fill="#555"/></svg>Denver, CO</span><span><svg width="10" height="10" viewBox="0 0 10 10"><path d="M5 .5l1.4 2.9 3.1.4-2.3 2.2.6 3.1L5 7.6 2.2 9.1l.6-3.1L.5 3.8l3.1-.4z" fill="#e7a019"/></svg><b>5.0</b> (24)</span></div>
      <div class="specs"><span><svg width="11" height="9" viewBox="0 0 12 10"><path d="M1 9V1M1 6h10v3M3 6V4h4v2" fill="none" stroke="#555"/></svg>Sleeps 6</span><span><svg width="11" height="9" viewBox="0 0 12 10"><rect x=".5" y="1.5" width="11" height="7" fill="none" stroke="#555"/><path d="M3 1.5v3M6 1.5v3M9 1.5v3" stroke="#555"/></svg>29 ft</span><span><svg width="12" height="9" viewBox="0 0 13 10"><rect x=".5" y=".5" width="9" height="6.5" fill="none" stroke="#555"/><path d="M9.5 3H12v4H9.5" fill="none" stroke="#555"/><circle cx="3" cy="8.5" r="1" fill="#555"/><circle cx="10" cy="8.5" r="1" fill="#555"/></svg>Class A</span></div>
      <div class="price">$189<small>/ night</small></div></div>
    </article>
    <article class="rv">
      <div class="img" role="img" aria-label="Travel trailer parked among tall pines" style="background:linear-gradient(170deg,#c9d2c6,#6f7f5a 50%,#3d4a2f)"><div class="dots"><i></i><i></i><i></i><i></i><i></i><i></i></div></div>
      <div class="body"><div class="title">2021 Brisco Pinecrest 26QB</div>
      <div class="meta"><span><svg width="9" height="11" viewBox="0 0 10 12"><path d="M5 11S1 6.6 1 4.3a4 4 0 0 1 8 0C9 6.6 5 11 5 11z" fill="none" stroke="#555"/><circle cx="5" cy="4.3" r="1.3" fill="#555"/></svg>Austin, TX</span><span><svg width="10" height="10" viewBox="0 0 10 10"><path d="M5 .5l1.4 2.9 3.1.4-2.3 2.2.6 3.1L5 7.6 2.2 9.1l.6-3.1L.5 3.8l3.1-.4z" fill="#e7a019"/></svg><b>4.9</b> (18)</span></div>
      <div class="specs"><span><svg width="11" height="9" viewBox="0 0 12 10"><path d="M1 9V1M1 6h10v3M3 6V4h4v2" fill="none" stroke="#555"/></svg>Sleeps 8</span><span><svg width="11" height="9" viewBox="0 0 12 10"><rect x=".5" y="1.5" width="11" height="7" fill="none" stroke="#555"/><path d="M3 1.5v3M6 1.5v3M9 1.5v3" stroke="#555"/></svg>28 ft</span><span><svg width="12" height="9" viewBox="0 0 13 10"><rect x=".5" y=".5" width="9" height="6.5" fill="none" stroke="#555"/><path d="M9.5 3H12v4H9.5" fill="none" stroke="#555"/><circle cx="3" cy="8.5" r="1" fill="#555"/><circle cx="10" cy="8.5" r="1" fill="#555"/></svg>Travel Trailer</span></div>
      <div class="price">$129<small>/ night</small></div></div>
    </article>
    <article class="rv">
      <div class="img" role="img" aria-label="Camper van beside a mountain lake" style="background:linear-gradient(170deg,#8fb3cf,#6d8b7c 50%,#4c5e3a)"><div class="dots"><i></i><i></i><i></i><i></i><i></i><i></i></div></div>
      <div class="body"><div class="title">2020 Korvel Nomad 170</div>
      <div class="meta"><span><svg width="9" height="11" viewBox="0 0 10 12"><path d="M5 11S1 6.6 1 4.3a4 4 0 0 1 8 0C9 6.6 5 11 5 11z" fill="none" stroke="#555"/><circle cx="5" cy="4.3" r="1.3" fill="#555"/></svg>Portland, OR</span><span><svg width="10" height="10" viewBox="0 0 10 10"><path d="M5 .5l1.4 2.9 3.1.4-2.3 2.2.6 3.1L5 7.6 2.2 9.1l.6-3.1L.5 3.8l3.1-.4z" fill="#e7a019"/></svg><b>5.0</b> (22)</span></div>
      <div class="specs"><span><svg width="11" height="9" viewBox="0 0 12 10"><path d="M1 9V1M1 6h10v3M3 6V4h4v2" fill="none" stroke="#555"/></svg>Sleeps 4</span><span><svg width="11" height="9" viewBox="0 0 12 10"><rect x=".5" y="1.5" width="11" height="7" fill="none" stroke="#555"/><path d="M3 1.5v3M6 1.5v3M9 1.5v3" stroke="#555"/></svg>21 ft</span><span><svg width="12" height="9" viewBox="0 0 13 10"><rect x=".5" y=".5" width="9" height="6.5" fill="none" stroke="#555"/><path d="M9.5 3H12v4H9.5" fill="none" stroke="#555"/><circle cx="3" cy="8.5" r="1" fill="#555"/><circle cx="10" cy="8.5" r="1" fill="#555"/></svg>Van</span></div>
      <div class="price">$159<small>/ night</small></div></div>
    </article>
    <article class="rv">
      <div class="img" role="img" aria-label="Class C motorhome among autumn trees and mountains" style="background:linear-gradient(170deg,#a9bcc8,#c48a3b 45%,#5f5a3a)"><div class="dots"><i></i><i></i><i></i><i></i><i></i><i></i></div></div>
      <div class="body"><div class="title">2023 Tarven Summit 29RX</div>
      <div class="meta"><span><svg width="9" height="11" viewBox="0 0 10 12"><path d="M5 11S1 6.6 1 4.3a4 4 0 0 1 8 0C9 6.6 5 11 5 11z" fill="none" stroke="#555"/><circle cx="5" cy="4.3" r="1.3" fill="#555"/></svg>Nashville, TN</span><span><svg width="10" height="10" viewBox="0 0 10 10"><path d="M5 .5l1.4 2.9 3.1.4-2.3 2.2.6 3.1L5 7.6 2.2 9.1l.6-3.1L.5 3.8l3.1-.4z" fill="#e7a019"/></svg><b>4.8</b> (21)</span></div>
      <div class="specs"><span><svg width="11" height="9" viewBox="0 0 12 10"><path d="M1 9V1M1 6h10v3M3 6V4h4v2" fill="none" stroke="#555"/></svg>Sleeps 7</span><span><svg width="11" height="9" viewBox="0 0 12 10"><rect x=".5" y="1.5" width="11" height="7" fill="none" stroke="#555"/><path d="M3 1.5v3M6 1.5v3M9 1.5v3" stroke="#555"/></svg>31 ft</span><span><svg width="12" height="9" viewBox="0 0 13 10"><rect x=".5" y=".5" width="9" height="6.5" fill="none" stroke="#555"/><path d="M9.5 3H12v4H9.5" fill="none" stroke="#555"/><circle cx="3" cy="8.5" r="1" fill="#555"/><circle cx="10" cy="8.5" r="1" fill="#555"/></svg>Class C</span></div>
      <div class="price">$175<small>/ night</small></div></div>
    </article>
  </div>

  <div class="abs btn-navy" style="left:531px;top:1729px;width:136px">VIEW ALL RV'S</div>
</section>

<section>
  <h2 class="abs h2" style="left:0;width:1200px;text-align:center;top:1856px;font-size:44px">Popular National Parks</h2>
  <div class="abs parks">
    <div class="park"><div class="photo" role="img" aria-label="Grand Canyon river gorge with red rock walls" style="background:linear-gradient(170deg,#b5604a,#7d3b2e 45%,#4c2a24)"></div><div class="shade"></div>
      <div class="info"><h4>Grand Canyon</h4><p>Stay from <b>$130 / Night</b></p><div class="pill">BOOK NOW</div></div></div>
    <div class="park"><div class="photo" role="img" aria-label="Yosemite valley with granite cliffs and pine forest" style="background:linear-gradient(170deg,#9aa6a0,#4d6a43 40%,#22351f)"></div><div class="shade"></div>
      <div class="info"><h4>Yosemite</h4><p>Stay from <b>$165 / night</b></p><div class="pill">BOOK NOW</div></div></div>
    <div class="park"><div class="photo" role="img" aria-label="Zion canyon with orange sandstone and green trees" style="background:linear-gradient(170deg,#b7a77e,#b9643b 40%,#5a5a30)"></div><div class="shade"></div>
      <div class="info"><h4>Zion</h4><p>Stay from <b>$150 / night</b></p><div class="pill">BOOK NOW</div></div></div>
    <div class="park"><div class="photo" role="img" aria-label="Yellowstone geyser over colourful hot spring" style="background:linear-gradient(175deg,#cfd5d6,#8fa6b0 30%,#d08a3a 60%,#8a4a24)"></div><div class="shade"></div>
      <div class="info"><h4>Yellowstone</h4><p>Stay from <b>$175 / night</b></p><div class="pill">BOOK NOW</div></div></div>
  </div>
  <div class="abs btn-navy" style="left:531px;top:2308px;width:136px">VIEW ALL</div>
</section>

<section>
  <h2 class="abs h2" style="left:115px;top:2430px">Explore Popular<br>RV Rental Destinations</h2>
  <p class="abs sub" style="left:115px;top:2542px">Hit the road to amazing places.</p>
  <div class="abs dest" style="top:2600px">
    <div>Atlanta, GA<span>751 RV rentals</span></div><div>Austin, TX<span>783 RV rentals</span></div><div>Boston, MA<span>351 RV rentals</span></div><div>Chicago, IL<span>455 RV rentals</span></div><div>Columbus, OH<span>410 RV rentals</span></div><div>Dallas, TX<span>715 RV rentals</span></div><div>Denver, CO<span>1,278 RV rentals</span></div>
    <div>Houston, TX<span>567 RV rentals</span></div><div>Kailua-Kona, HI<span>148 RV rentals</span></div><div>Kauai, HI<span>82 RV rentals</span></div><div>Las Vegas, NV<span>436 RV rentals</span></div><div>Los Angeles, CA<span>2,834 RV rentals</span></div><div>Maui, HI<span>149 RV rentals</span></div><div>Miami, FL<span>483 RV rentals</span></div>
    <div>Nashville, TN<span>311 RV rentals</span></div><div>New York, NY<span>575 RV rentals</span></div><div>Oklahoma City, OK<span>139 RV rentals</span></div><div>Orlando, FL<span>1,326 RV rentals</span></div><div>Phoenix, AZ<span>953 RV rentals</span></div><div>Portland, OR<span>645 RV rentals</span></div><div>Raleigh, NC<span>259 RV rentals</span></div>
    <div>San Antonio, TX<span>690 RV rentals</span></div><div>San Diego, CA<span>2,093 RV rentals</span></div><div>San Francisco, CA<span>1,447 RV rentals</span></div><div>Seattle, WA<span>790 RV rentals</span></div>
  </div>
</section>

<section>
  <h2 class="abs h2" style="left:115px;top:2876px">Explore By City</h2>
  <div class="abs dest" style="top:2970px;row-gap:23px">
    <div>Alabama<span>516 RV rentals</span></div><div>Alaska<span>859 RV rentals</span></div><div>Arizona<span>1,144 RV rentals</span></div><div>Arkansas<span>86 RV rentals</span></div><div>California<span>6,292 RV rentals</span></div><div>Colorado<span>1,485 RV rentals</span></div><div>Connecticut<span>451 RV rentals</span></div>
    <div>Florida<span>2,453 RV rentals</span></div><div>Georgia<span>1,029 RV rentals</span></div><div>Hawaii<span>433 RV rentals</span></div><div>Idaho<span>652 RV rentals</span></div><div>Illinois<span>114 RV rentals</span></div><div>Indiana<span>242 RV rentals</span></div><div>Iowa<span>106 RV rentals</span></div>
    <div>Kentucky<span>205 RV rentals</span></div><div>Louisiana<span>269 RV rentals</span></div><div>Maine<span>53 RV rentals</span></div><div>Maryland<span>630 RV rentals</span></div><div>Massachusetts<span>369 RV rentals</span></div><div>Michigan<span>1,292 RV rentals</span></div><div>Minnesota<span>597 RV rentals</span></div>
    <div>Missouri<span>453 RV rentals</span></div><div>Montana<span>286 RV rentals</span></div><div>Nebraska<span>90 RV rentals</span></div><div>Nevada<span>1,029 RV rentals</span></div><div>New Hampshire<span>333 RV rentals</span></div><div>New Jersey<span>587 RV rentals</span></div><div>New Mexico<span>181 RV rentals</span></div>
    <div>North Carolina<span>1,169 RV rentals</span></div><div>North Dakota<span>55 RV rentals</span></div><div>Ohio<span>458 RV rentals</span></div><div>Oklahoma<span>273 RV rentals</span></div><div>Oregon<span>1,051 RV rentals</span></div><div>Pennsylvania<span>250 RV rentals</span></div><div>Rhode Island<span>350 RV rentals</span></div>
    <div>South Dakota<span>73 RV rentals</span></div><div>Tennessee<span>626 RV rentals</span></div><div>Texas<span>2,651 RV rentals</span></div><div>Utah<span>1,039 RV rentals</span></div><div>Vermont<span>315 RV rentals</span></div><div>Virginia<span>635 RV rentals</span></div><div>Washington<span>681 RV rentals</span></div>
    <div>West Virginia<span>220 RV rentals</span></div><div>Wisconsin<span>367 RV rentals</span></div><div>Wyoming<span>97 RV rentals</span></div>
  </div>
</section>

<section class="abs band">
  <div class="ring" style="left:716px;top:3px;width:320px;height:320px"></div>
  <div class="ring" style="left:746px;top:33px;width:260px;height:260px"></div>
  <div class="ring" style="left:771px;top:58px;width:210px;height:210px;border-color:rgba(255,255,255,.3)"></div>
  <h2>List your RV. Set your<br>price. Keep every dollar.</h2>
  <p>One flat monthly fee, however many nights you book. No commission, no surprise cuts — just your rig, your calendar, your earnings.</p>
  <div class="pill">LIST YOUR RV</div>
  <div class="stat"><strong>100%</strong><span>OF RENTAL<br>INCOME, YOURS</span></div>
</section>

<footer class="abs footer">
  <div class="fbrand"><span class="dot"></span>Zandoprik.com</div>
  <div class="tag">Your RV. Your Adventure.<br>Your Earnings.</div>
  <div class="rule"></div>
  <div class="dl">DOWNLOAD ZANDOPRIK.COM APP</div>
  <div class="store" style="left:113px;width:76px"></div>
  <div class="store" style="left:197px;width:80px"></div>

  <div class="col" style="left:428px"><h5>Explore</h5><ul><li>Find an RV</li><li>Browse Destinations</li><li>Featured RVs</li><li>How It Works</li><li>Delivery &amp; On-Site Stays</li></ul></div>
  <div class="col" style="left:610px"><h5>For Owners</h5><ul><li>List Your RV</li><li>Become a Host</li><li>Owner Benefits</li><li>Pricing</li><li>Host Resources</li><li>Owner FAQ</li></ul></div>
  <div class="col" style="left:792px"><h5>For Renters</h5><ul><li>Search RVs</li><li>Popular Destinations</li><li>How to Rent</li><li>Booking Guide</li><li>Renter FAQ</li></ul></div>
  <div class="col" style="left:974px"><h5>Support</h5><ul><li>Help Center</li><li>Contact Us</li><li>Safety</li><li>Terms &amp; Conditions</li><li>Privacy Policy</li></ul></div>

  <div class="bottom"></div>
  <div class="copy">© 2026 Zandoprik.com. All rights reserved.</div>
  <div class="social"><i></i><i class="round"></i><i></i><i></i></div>
</footer>

</div>
</body>
</html>
```